Velmora Flowers Florist Flyer

We are requiring a flyer that advertises and promotes our new business. We specialise in weddings and events but would also like to branch out to corporates and an online subscription. Our brand is feminine/romantic with a touch of elegance and luxury. Our main colour schemes are white, black, gold and pale pink. Instagram: Velmora_flowers and website www.velmoraflowers.com.au
Target Market(s)
brides to be, females
Industry/Entity Type
Florist
Font styles to use
Sans Serif
Script
Other font styles liked:
- The Carpenter
Colors
ffffff
000000
333333
Requirements
Must have
- Feminine/romantic feel, through use of theme colours and elegant font
- our contact details Ph: 0478215096
- email address: contactus@velmoraflowers.com.au
Nice to have
- a description of us willing to work with clients to create their dream wedding flowers. That we offer consultations and no obligation quotes.

```html
<!DOCTYPE html>
<html lang="en">
<head>
<meta charset="utf-8">
<title>Velmora Flowers Flyer</title>
<link href="https://fonts.googleapis.com/css2?family=Libre+Baskerville:wght@400;700&family=Lato:wght@400;700&family=Pinyon+Script&display=swap" rel="stylesheet">
<style>
  :root{
    --stage:#8c8c8c;
    --paper:#ffffff;
    --ink:#000000;
    --text:#333333;
    --pink:#e99ac6;
    --pink-deep:#d9508f;
    --pink-title:#d74d8c;
    --pink-soft:#f2b8d6;
  }
  *{margin:0;padding:0;box-sizing:border-box}
  html,body{width:1200px;height:1200px;overflow:hidden;background:var(--stage)}
  .flyer{position:absolute;left:246px;top:103px;width:708px;height:994px;background:var(--paper);overflow:hidden;font-family:'Lato',sans-serif;color:var(--text)}
  .flyer-art{position:absolute;inset:0}
  .brand{position:absolute;left:36px;top:42px;width:220px;font-family:'Libre Baskerville',serif;font-weight:400;color:var(--ink);line-height:1}
  .brand-name{display:block;font-size:44px;letter-spacing:0.5px}
  .brand-sub{display:block;margin-top:22px;font-size:14px;letter-spacing:13.5px}
  .title{position:absolute;left:0;width:708px;top:520px;text-align:center;font-family:'Libre Baskerville',serif;font-weight:700;font-size:45px;letter-spacing:9px;color:var(--ink);white-space:nowrap}
  .tagline{position:absolute;left:0;width:708px;top:575px;text-align:center;font-family:'Libre Baskerville',serif;font-size:22.5px;color:var(--pink-title);white-space:nowrap}
  .about-tab{position:absolute;left:0;top:615px;width:162px;height:31px;background:var(--pink);border-radius:0 16px 16px 0;color:#fff;font-weight:700;font-size:19px;padding-left:37px;line-height:31px}
  .quote{position:absolute;left:30px;top:655px;width:310px;font-family:'Pinyon Script',cursive;font-size:21px;line-height:21px;color:var(--ink)}
  .quote-author{position:absolute;left:33px;top:728px;font-size:13px;color:var(--ink)}
  .about-copy{position:absolute;left:30px;top:761px;width:310px;font-size:11.2px;line-height:13.8px;color:var(--text)}
  .about-copy p+p{margin-top:9px}
  .services{position:absolute;left:368px;top:629px;width:310px;height:210px;border-radius:22px;overflow:hidden;background:linear-gradient(#ec9fca,#d9508f)}
  .services-head{height:36px;background:var(--ink);color:#fff;text-align:center;font-family:'Libre Baskerville',serif;font-size:21px;line-height:40px;letter-spacing:0.5px}
  .service{position:absolute;width:140px;text-align:center;color:#fff;font-weight:700;font-size:16px}
  .service svg{display:block;margin:0 auto 5px}
  .call{position:absolute;left:38px;top:934px;font-weight:700;font-size:28px;color:#fff}
  .contact{position:absolute;left:448px;font-weight:700;font-size:12.6px;line-height:14px;color:#fff;white-space:nowrap}
</style>
</head>
<body>
<main class="flyer">
  <svg class="flyer-art" width="708" height="994" viewBox="0 0 708 994">
    <defs>
      <linearGradient id="venue" x1="0" y1="0" x2="1" y2="1">
        <stop offset="0" stop-color="#3b3a35"/>
        <stop offset="0.45" stop-color="#5d5a4e"/>
        <stop offset="0.75" stop-color="#d9c4ae"/>
        <stop offset="1" stop-color="#6b5a45"/>
      </linearGradient>
      <linearGradient id="bouquetWarm" x1="0" y1="0" x2="1" y2="1">
        <stop offset="0" stop-color="#6d7a4e"/><stop offset="0.5" stop-color="#c8a68a"/><stop offset="1" stop-color="#8a2a2a"/>
      </linearGradient>
      <linearGradient id="bouquetWhite" x1="0" y1="0" x2="0" y2="1">
        <stop offset="0" stop-color="#a09c92"/><stop offset="0.5" stop-color="#e8eadf"/><stop offset="1" stop-color="#8d8a83"/>
      </linearGradient>
    </defs>
    <rect class="venue-photo" role="img" aria-label="Reception venue with tall arrangements of peach roses and white blooms on the tables" x="0" y="0" width="708" height="470" fill="url(#venue)"/>
    <path class="header-swoosh" d="M0 0 H424 C372 30 332 100 292 150 C242 205 152 226 82 212 C42 203 15 188 0 172 Z" fill="var(--paper)"/>
    <path class="pink-wave" d="M0 393 C60 440 150 480 260 460 C380 440 480 360 600 310 C650 290 690 300 708 310 V470 C640 480 560 490 480 480 C350 470 200 490 100 490 C50 490 20 485 0 480 Z" fill="var(--pink)"/>
    <path class="white-base" d="M0 415 C60 455 150 490 260 475 C380 460 500 440 600 450 C650 455 690 460 708 465 V994 H0 Z" fill="var(--paper)"/>
    <ellipse cx="398" cy="401" rx="104" ry="110" fill="var(--pink-soft)"/>
    <ellipse class="bouquet-photo" role="img" aria-label="Bouquet of red and cream roses with anthurium and foliage" cx="398" cy="401" rx="96" ry="102" fill="url(#bouquetWarm)"/>
    <ellipse cx="610" cy="373" rx="98" ry="126" fill="var(--pink-soft)"/>
    <ellipse class="bouquet-photo" role="img" aria-label="White rose bridal bouquet tied with ribbon" cx="610" cy="373" rx="90" ry="118" fill="url(#bouquetWhite)"/>
    <line x1="353" y1="700" x2="353" y2="880" stroke="#e4e4e4" stroke-width="2"/>
    <path class="footer-band" d="M0 880 C80 920 170 935 280 915 C420 890 520 840 620 855 C660 862 690 880 708 895 V994 H0 Z" fill="var(--ink)"/>
    <rect x="425" y="916" width="15" height="10" fill="#fff"/>
    <path d="M425 916 L432.5 922 L440 916" fill="none" stroke="#000" stroke-width="1.3"/>
    <circle cx="432" cy="954" r="6" fill="none" stroke="#fff" stroke-width="1.3"/>
    <ellipse cx="432" cy="954" rx="2.6" ry="6" fill="none" stroke="#fff" stroke-width="1"/>
    <line x1="426" y1="954" x2="438" y2="954" stroke="#fff" stroke-width="1"/>
  </svg>

  <div class="brand"><span class="brand-name">Velmora</span><span class="brand-sub">FLOWERS</span></div>

  <h1 class="title">VELMORA FLOWERS</h1>
  <p class="tagline">Creating stunning Flowers for Weddings and Events</p>

  <div class="about-tab">ABOUT US</div>
  <p class="quote">Design is not making beauty, beauty emerges from selection, affinities, integration, love.</p>
  <p class="quote-author">___ARDEN HALE</p>
  <div class="about-copy">
    <p>For generations we've been creating flowers for family and friends. Over the years this has been our test bed for creating our design pieces for weddings and events. Now we want to make our beautiful creations available to everyone.</p>
    <p>Our designers have had extensive backgrounds, from owning a florist, to chocolate bouquet design and creations. Our friends and family loved working with our designers to create their perfect flower design, no matter what the event was.</p>
  </div>

  <section class="services">
    <h2 class="services-head">SERVICES</h2>
    <div class="service" style="left:16px;top:58px">
      <svg width="40" height="40" viewBox="0 0 40 40"><circle cx="20" cy="20" r="19" fill="#fff" stroke="#f0bcd8" stroke-width="2"/><path d="M20 29 C10 22 10 14 15 13 C18 12.5 20 15 20 16 C20 15 22 12.5 25 13 C30 14 30 22 20 29Z" fill="none" stroke="#e07fb0" stroke-width="2"/></svg>Weddings</div>
    <div class="service" style="left:159px;top:58px">
      <svg width="40" height="40" viewBox="0 0 40 40"><circle cx="20" cy="20" r="19" fill="#fff" stroke="#f0bcd8" stroke-width="2"/><rect x="12" y="13" width="16" height="14" rx="1.5" fill="none" stroke="#e07fb0" stroke-width="1.6"/><line x1="12" y1="17" x2="28" y2="17" stroke="#e07fb0" stroke-width="1.6"/><line x1="16" y1="11" x2="16" y2="14" stroke="#e07fb0" stroke-width="1.6"/><line x1="24" y1="11" x2="24" y2="14" stroke="#e07fb0" stroke-width="1.6"/></svg>Events</div>
    <div class="service" style="left:16px;top:135px">
      <svg width="40" height="40" viewBox="0 0 40 40"><circle cx="20" cy="20" r="19" fill="#fff" stroke="#f0bcd8" stroke-width="2"/><rect x="11" y="15" width="18" height="13" rx="1.5" fill="#e07fb0"/><rect x="16" y="11.5" width="8" height="4" rx="1" fill="none" stroke="#e07fb0" stroke-width="1.6"/><line x1="11" y1="20" x2="29" y2="20" stroke="#fff" stroke-width="1.2"/></svg>Businesses</div>
    <div class="service" style="left:159px;top:135px">
      <svg width="40" height="40" viewBox="0 0 40 40"><circle cx="20" cy="20" r="19" fill="#fff" stroke="#f0bcd8" stroke-width="2"/><path d="M10 21 L20 12 L30 21" fill="none" stroke="#e07fb0" stroke-width="2.4"/><path d="M13.5 19.5 V29 H18 V24 H22 V29 H26.5 V19.5" fill="#e07fb0"/></svg>Home</div>
  </section>

  <p class="call">Call now: 0478215096</p>
  <p class="contact" style="top:914px">contactus@velmoraflowers.com.au</p>
  <p class="contact" style="top:947px">www.velmoraflowers.com.au</p>
</main>
</body>
</html>
```